WordPress Site Design and Code for Technology Consulting Startup

We need a WordPress design and code to a new site on Tallow Bay. We have the logo and colors ready. The site will be a brochure site with a CONTACT page that contains a form that the prospective client fills out. The other pages would be ABOUT / SERVICES (3 option drop-down) / SUPPORT. The site should be appropriate for an IT Consulting / IT Managed Services / IT Project Management services in the Chicago area.

Across small, medium, large businesses.

Technology, network infrastructure, IT.

Coded - Design and coding required

5+ page

• I prefer mid-modern / simple / art deco / minimalist.

```html
<!DOCTYPE html>
<html lang="en">
<head>
<meta charset="utf-8">
<title>Corvane — IT Consulting in the Chicago Area</title>
<link href="https://fonts.googleapis.com/css2?family=Krona+One&family=Poppins:ital,wght@0,400;0,500;0,600;0,700;1,400&display=swap" rel="stylesheet">
<style>
:root{
  --orange:#f7770f;
  --orange-soft:#f8852a;
  --teal:#0e8fa3;
  --ink:#1e2a33;
  --body:#4f5a63;
  --mist:#e7f5f6;
  --night:#333333;
  --white:#ffffff;
}
*{margin:0;padding:0;box-sizing:border-box}
html,body{width:1200px;height:3971px;overflow:hidden}
body{position:relative;font-family:"Poppins",sans-serif;color:var(--body);background:var(--white)}
.abs{position:absolute}
.display{font-family:"Krona One",sans-serif;font-weight:400;color:var(--ink);letter-spacing:.5px;white-space:nowrap}
.eyebrow{font-family:"Poppins",sans-serif;font-weight:600;font-size:14px;letter-spacing:4px;color:var(--teal)}
.center{left:0;width:1200px;text-align:center}
.btn{display:flex;align-items:center;justify-content:center;gap:6px;font-weight:600;font-size:12px;text-transform:uppercase;text-decoration:none}
.btn-solid{background:var(--orange);color:var(--white)}
.btn-line{border:1.5px solid var(--orange);color:var(--orange);background:var(--white)}
.brand{display:flex;align-items:center;gap:8px;font-family:"Poppins",sans-serif;font-weight:700;font-size:24px;letter-spacing:1px;color:var(--orange)}
.brand-mark{width:20px;height:20px;background:var(--orange)}
.divider-mark{display:flex;align-items:center;gap:8px}
.divider-mark i{display:block;width:34px;height:1px;background:#c9d3d8}
.divider-mark b{display:block;width:12px;height:12px;background:var(--orange)}
.photo{position:absolute}
.nav a{position:absolute;top:34px;font-size:11px;color:var(--ink);text-decoration:none}
.para{font-size:12.5px;line-height:24px;color:var(--body)}
.card{position:absolute;width:279px;height:295px;overflow:hidden}
.card-label{position:absolute;left:20px;color:var(--white);font-weight:600;font-size:16px;line-height:20px;text-transform:uppercase}
.card-go{position:absolute;right:0;width:40px;height:40px;border-radius:50%;background:var(--orange);display:flex;align-items:center;justify-content:center}
.avatar{position:absolute;border-radius:50%;border:3px solid var(--white);box-shadow:0 3px 10px rgba(0,0,0,.15)}
.field{position:absolute;border:1px solid #dfe4e7;font-size:14px;color:#7a848b;padding:16px 22px;background:var(--white)}
.info-icon{position:absolute;left:162px;width:44px;height:44px;border-radius:50%;background:var(--orange);display:flex;align-items:center;justify-content:center}
.foot-h{position:absolute;color:var(--white);font-weight:600;font-size:15px}
.foot-a{position:absolute;color:#e8e8e8;font-size:11.5px;text-decoration:none;text-transform:uppercase}
.social{position:absolute;top:3832px;width:12px;height:12px;border-radius:50%;background:#dcdcdc}
</style>
</head>
<body>

<section class="hero">
  <div class="photo" role="img" aria-label="Photo of a team of five consultants gathered around a laptop at a bright office table" style="left:0;top:0;width:1200px;height:705px;background:linear-gradient(180deg,#ffffff 0%,#f7f8f8 30%,#d9c8b6 60%,#7d6f66 100%)"></div>
  <svg class="abs" style="left:0;top:560px" width="1200" height="160" viewBox="0 0 1200 160">
    <polygon points="0,145 1200,30 1200,140 0,160" fill="#e7f5f6"/>
    <polygon points="0,160 1200,140 1200,160" fill="#ffffff"/>
    <polygon points="0,120 560,160 0,160" fill="#ffffff"/>
  </svg>
  <header>
    <div class="brand abs" style="left:162px;top:24px"><span class="brand-mark"></span>CORVANE</div>
    <nav class="nav">
      <a style="left:555px">HOME</a>
      <a style="left:632px">ABOUT</a>
      <a style="left:714px">SERVICES&nbsp;&#8964;</a>
      <a style="left:826px">SUPPORT</a>
    </nav>
    <a class="btn btn-line abs" style="left:920px;top:25px;width:118px;height:33px">Contact &rarr;</a>
  </header>
  <p class="eyebrow abs center" style="top:99px">WE PROVIDE</p>
  <h1 class="display abs center" style="top:126px;font-size:26px;line-height:38px">IT CONSULTING / IT MANAGED SERVICES /<br>IT PROJECT MANAGEMENT SERVICES IN<br>THE CHICAGO AREA</h1>
  <a class="btn btn-solid abs" style="left:529px;top:250px;width:142px;height:40px;font-size:13px">Contact &rarr;</a>
  <div class="abs" style="left:578px;top:619px;width:44px;height:44px;border-radius:50%;background:#fff;box-shadow:0 4px 12px rgba(0,0,0,.12);display:flex;align-items:center;justify-content:center">
    <svg width="12" height="8" viewBox="0 0 12 8"><path d="M1 1l5 5 5-5" fill="none" stroke="#1e2a33" stroke-width="1.6"/></svg>
  </div>
</section>

<section class="about">
  <div class="photo" role="img" aria-label="Photo of four colleagues smiling around a laptop" style="left:295px;top:783px;width:310px;height:261px;background:linear-gradient(160deg,#e9ecee,#9aa7b0 55%,#4d5a66)"></div>
  <div class="photo" role="img" aria-label="Photo of a team working at laptops in an office" style="left:167px;top:956px;width:231px;height:227px;background:linear-gradient(160deg,#9fb3bd,#4c6472 60%,#2e3e4a)"></div>
  <div class="abs" style="left:125px;top:887px;width:211px;height:205px;border:3px solid var(--orange)"></div>
  <div class="photo" role="img" aria-label="Decorative zigzag pattern" style="left:413px;top:1075px;width:199px;height:105px;background:linear-gradient(180deg,#f6e1c4,#f3d7b2)"></div>
  <p class="eyebrow abs" style="left:674px;top:810px">ABOUT US</p>
  <h2 class="display abs" style="left:674px;top:836px;font-size:30px">WHO WE ARE</h2>
  <div class="divider-mark abs" style="left:674px;top:881px"><b></b></div>
  <p class="para abs" style="left:674px;top:918px;width:370px">Lorem ipsum dolor sit amet, consetetur sadipscing elitr, sed diam nonumy eirmod tempor invidunt ut labore et dolore magna aliquyam erat, sed diam voluptua. At vero eos et accusam et justo duo dolores et ea rebum.</p>
  <p class="para abs" style="left:674px;top:1023px;width:370px">Lorem ipsum dolor sit amet, consetetur sadipscing elitr, sed diam nonumy eirmod tempor invidunt ut labore et dolore magna aliquyam erat, sed diam voluptua.</p>
  <a class="btn btn-solid abs" style="left:674px;top:1113px;width:193px;height:37px;font-size:11.5px">Read more about us &rarr;</a>
</section>

<section class="services">
  <svg class="abs" style="left:0;top:1270px" width="1200" height="650" viewBox="0 0 1200 650">
    <polygon points="0,0 600,0 1200,0 1200,550 600,640 0,545" fill="#e7f5f6"/>
    <polygon points="0,0 600,0 1200,0 1200,14 600,3 0,12" fill="#ffffff"/>
    <polygon points="0,14 298,52 0,98" fill="#0e8fa3"/>
    <polygon points="1200,14 902,52 1200,98" fill="#f7770f"/>
  </svg>
  <p class="eyebrow abs center" style="top:1370px">OUR SERVICES</p>
  <h2 class="display abs center" style="top:1396px;font-size:30px">WHAT WE DO</h2>
  <div class="divider-mark abs" style="left:566px;top:1439px"><i></i><b></b><i></i></div>

  <div class="card" style="left:162px;top:1485px">
    <div class="photo" role="img" aria-label="Photo of two businessmen reviewing a laptop" style="inset:0;background:linear-gradient(150deg,#dfe3e6,#6f7b86 55%,#2e3944)"></div>
    <svg class="abs" style="left:0;top:0" width="279" height="295"><polygon points="0,295 0,205 279,180 279,232 120,295" fill="#0e8fa3"/></svg>
    <div class="card-label" style="top:212px">IT<br>CONSULTING</div>
    <div class="card-go" style="top:207px"><svg width="8" height="12"><path d="M2 2l4 4-4 4" fill="none" stroke="#fff" stroke-width="1.6"/></svg></div>
  </div>
  <div class="card" style="left:461px;top:1485px">
    <div class="photo" role="img" aria-label="Illustration of a hand touching a glowing digital network" style="inset:0;background:linear-gradient(150deg,#0d5d73,#1c9fb4 50%,#083b4d)"></div>
    <svg class="abs" style="left:0;top:0" width="279" height="295"><polygon points="0,295 0,205 279,180 279,232 120,295" fill="#0e8fa3"/></svg>
    <div class="card-label" style="top:213px">IT MANAGED<br>SERVICES</div>
    <div class="card-go" style="top:207px"><svg width="8" height="12"><path d="M2 2l4 4-4 4" fill="none" stroke="#fff" stroke-width="1.6"/></svg></div>
  </div>
  <div class="card" style="left:759px;top:1485px">
    <div class="photo" role="img" aria-label="Photo of a presenter at a whiteboard in a meeting" style="inset:0;background:linear-gradient(150deg,#eef0f1,#b4bcc2 50%,#55606a)"></div>
    <svg class="abs" style="left:0;top:0" width="279" height="295"><polygon points="0,295 0,205 279,180 279,232 120,295" fill="#0e8fa3"/></svg>
    <div class="card-label" style="top:198px">PROJECT<br>MANAGEMENT<br>SERVICES</div>
    <div class="card-go" style="top:207px"><svg width="8" height="12"><path d="M2 2l4 4-4 4" fill="none" stroke="#fff" stroke-width="1.6"/></svg></div>
  </div>
</section>

<section class="cta">
  <svg class="abs" style="left:0;top:1814px" width="1200" height="482" viewBox="0 0 1200 482">
    <polygon points="0,0 600,97 1200,0 1200,482 600,390 0,482" fill="#f7770f"/>
  </svg>
  <h2 class="display abs" style="left:162px;top:1992px;font-size:26px;line-height:42px;color:#fff">ARE YOU READY?<br>BOOK APPOINTMENT NOW!</h2>
  <p class="abs" style="left:162px;top:2082px;font-size:18px;color:#fff">Get Your Quote or Call: (123) 456-7890</p>
  <div class="abs" role="img" aria-label="Decorative hand-drawn looping arrow" style="left:665px;top:2055px;width:165px;height:55px;background:var(--orange-soft)"></div>
  <a class="btn btn-line abs" style="left:843px;top:2029px;width:187px;height:40px;border-color:#fff;font-size:12.5px">Contact us now &rarr;</a>
</section>

<section class="testimonials">
  <p class="eyebrow abs center" style="top:2330px">TESTIMONIALS</p>
  <h2 class="display abs center" style="top:2355px;font-size:28px">WHAT OUR CLIENTS SAY</h2>
  <div class="divider-mark abs" style="left:546px;top:2399px"><i></i><b></b><i></i></div>
  <div class="abs" style="left:370px;top:2370px;font-family:Georgia,serif;font-size:330px;line-height:1;color:#f1f3f4">&ldquo;</div>
  <div class="abs" style="left:539px;top:2490px;width:122px;height:122px;border-radius:50%;border:1.5px solid var(--orange);background:#fff"></div>
  <div class="photo" role="img" aria-label="Portrait of the featured client" style="left:548px;top:2499px;width:104px;height:104px;border-radius:50%;background:linear-gradient(160deg,#cfd9e2,#6b7f92)"></div>
  <div class="avatar" role="img" aria-label="Client portrait" style="left:228px;top:2497px;width:44px;height:44px;background:#a98a7a"></div>
  <div class="avatar" role="img" aria-label="Client portrait" style="left:66px;top:2578px;width:44px;height:44px;background:#5a5d5e"></div>
  <div class="avatar" role="img" aria-label="Client portrait" style="left:222px;top:2686px;width:66px;height:66px;background:#9db0bd"></div>
  <div class="avatar" role="img" aria-label="Client portrait" style="left:-1px;top:2774px;width:86px;height:86px;background:#b88f78"></div>
  <div class="avatar" role="img" aria-label="Client portrait" style="left:905px;top:2547px;width:56px;height:56px;background:#8fa2b2"></div>
  <div class="avatar" role="img" aria-label="Client portrait" style="left:1103px;top:2488px;width:74px;height:74px;background:#c49a84"></div>
  <div class="avatar" role="img" aria-label="Client portrait" style="left:913px;top:2779px;width:56px;height:56px;background:#8a6558"></div>
  <div class="avatar" role="img" aria-label="Client portrait" style="left:1109px;top:2829px;width:68px;height:68px;background:#7b8a96"></div>
  <p class="abs center" style="top:2648px;font-size:14px;font-style:italic;line-height:31.5px;color:#4f5a63">Lorem ipsum dolor sit amet, consetetur sadipscing elitr, sed diam<br>nonumy eirmod tempor invidunt ut labore et dolore magna aliquyam<br>erat, sed diam voluptua. At vero eos et accusam et</p>
  <p class="abs center" style="top:2770px;font-size:15px;font-weight:600;color:var(--orange)">LOREM IPSUM DOLOR</p>
  <p class="abs center" style="top:2800px;font-size:12px;color:#4f5a63">Lorem ipsum dolor</p>
  <svg class="abs" style="left:508px;top:2843px" width="184" height="16" viewBox="0 0 184 16">
    <path d="M20 8H2M7 3L2 8l5 5" fill="none" stroke="#9aa3a9" stroke-width="1.4"/>
    <circle cx="62" cy="8" r="3.5" fill="#d4d9dc"/><circle cx="77" cy="8" r="3.5" fill="#d4d9dc"/><circle cx="92" cy="8" r="3.5" fill="#f7770f"/><circle cx="107" cy="8" r="3.5" fill="#d4d9dc"/><circle cx="122" cy="8" r="3.5" fill="#d4d9dc"/>
    <path d="M164 8h18M177 3l5 5-5 5" fill="none" stroke="#f7770f" stroke-width="1.4"/>
  </svg>
</section>

<section class="contact">
  <svg class="abs" style="left:0;top:2945px" width="1200" height="550" viewBox="0 0 1200 550">
    <polygon points="0,100 600,40 1200,0 1200,550 0,550" fill="#e7f5f6"/>
    <rect x="0" y="548" width="1200" height="2" fill="#333333"/>
  </svg>
  <div class="abs" style="left:0;top:3493px;width:1200px;height:478px;background:var(--night)"></div>

  <p class="eyebrow abs" style="left:162px;top:3095px">CONTACT US</p>
  <h2 class="display abs" style="left:162px;top:3122px;font-size:28px">GET IN TOUCH</h2>
  <div class="divider-mark abs" style="left:162px;top:3170px"><b></b><i></i></div>

  <div class="info-icon" style="top:3226px"><svg width="18" height="20" viewBox="0 0 18 20"><path d="M9 19s7-6.5 7-11A7 7 0 0 0 2 8c0 4.5 7 11 7 11z" fill="none" stroke="#fff" stroke-width="1.5"/><circle cx="9" cy="8" r="2.5" fill="none" stroke="#fff" stroke-width="1.5"/></svg></div>
  <p class="abs" style="left:222px;top:3222px;font-size:13px;line-height:27px;color:var(--ink)">123, Building Name, Street<br>City, State XY 123456</p>
  <div class="info-icon" style="top:3306px"><svg width="18" height="18" viewBox="0 0 18 18"><path d="M4 1l3 4-2 2c1 2 3 4 5 5l2-2 4 3-2 3C8 16 2 10 1 4z" fill="none" stroke="#fff" stroke-width="1.5"/></svg></div>
  <p class="abs" style="left:222px;top:3305px;font-size:13px;color:var(--ink)">Phone</p>
  <p class="abs" style="left:222px;top:3330px;font-size:17px;font-weight:600;letter-spacing:1px;color:var(--ink)">(123) 456 7890</p>
  <div class="info-icon" style="top:3390px"><svg width="20" height="14" viewBox="0 0 20 14"><rect x="1" y="1" width="18" height="12" fill="none" stroke="#fff" stroke-width="1.5"/><path d="M1 1l9 7 9-7" fill="none" stroke="#fff" stroke-width="1.5"/></svg></div>
  <p class="abs" style="left:222px;top:3390px;font-size:13px;color:var(--ink)">Email</p>
  <p class="abs" style="left:222px;top:3417px;font-size:13.5px;color:var(--ink)">info@corvane.com</p>

  <form class="abs" style="left:552px;top:3081px;width:486px;height:547px;background:#fff;border-radius:14px;box-shadow:0 6px 24px rgba(0,0,0,.06)">
    <p class="eyebrow abs" style="left:0;width:486px;text-align:center;top:64px">CONTACT FORM</p>
    <h3 class="display abs" style="left:0;width:486px;text-align:center;top:90px;font-size:27px">QUICK INQUIRY</h3>
    <div class="divider-mark abs" style="left:189px;top:137px"><i></i><b></b><i></i></div>
    <div class="field" style="left:43px;top:176px;width:188px;height:45px">First Name</div>
    <div class="field" style="left:253px;top:176px;width:188px;height:45px">Last Name</div>
    <div class="field" style="left:43px;top:242px;width:398px;height:46px">Email</div>
    <div class="field" style="left:43px;top:310px;width:398px;height:117px">Message</div>
    <div class="btn btn-solid abs" style="left:176px;top:450px;width:134px;height:37px">Submit &rarr;</div>
  </form>
</section>

<footer>
  <div class="brand abs" style="left:162px;top:3706px;color:#fff"><span class="brand-mark" style="background:#fff"></span>CORVANE</div>
  <p class="abs" style="left:162px;top:3752px;width:200px;font-size:12px;line-height:24px;color:#e8e8e8">Lorem ipsum dolor sit amet, consetetur sadipscing elitr, sed diam nonumy eirmod tempor</p>
  <span class="social" style="left:161px"></span><span class="social" style="left:192px"></span><span class="social" style="left:226px"></span><span class="social" style="left:262px"></span>

  <h4 class="foot-h" style="left:404px;top:3705px">QUICK LINKS</h4>
  <a class="foot-a" style="left:404px;top:3742px">Home</a>
  <a class="foot-a" style="left:404px;top:3779px">About</a>
  <a class="foot-a" style="left:404px;top:3815px">Support</a>
  <a class="foot-a" style="left:404px;top:3852px">Contact</a>

  <h4 class="foot-h" style="left:549px;top:3705px">SERVICES</h4>
  <a class="foot-a" style="left:549px;top:3742px">IT Consulting</a>
  <a class="foot-a" style="left:549px;top:3779px">IT Managed Services</a>
  <a class="foot-a" style="left:549px;top:3815px">Project Management Services</a>

  <h4 class="foot-h" style="left:788px;top:3705px">NEWSLETTER SIGNUP</h4>
  <div class="abs" style="left:788px;top:3744px;width:250px;height:36px;background:#fff;font-size:12px;color:#6f777d;padding:10px 22px">Enter email address</div>
  <div class="btn btn-solid abs" style="left:788px;top:3796px;width:106px;height:34px">Sign up &rarr;</div>

  <div class="abs" style="left:0;top:3921px;width:1200px;height:1px;background:#4a4a4a"></div>
  <p class="abs center" style="top:3938px;font-size:12px;color:#e0e0e0">Copyright 2023 CORVANE. All rights reserved.</p>
</footer>

</body>
</html>
```